Halvering & Partners, LLC Business Card 2016

We need a new business card design for a very important trade show coming up.

We are a compliance Consulting Firm. Our clients are stock brokerage firms and investment advisers.

I would like our logo on both sides of the card.

Info in the front of the card shold include:

Logo
First & Last Name
Title
Office #
Cell #
Email
Company Address (42 W. Calloway Blvd., Suite 300 Pasadena, CA 91847

Back of the card should include the logo and url: www.halveringpartnersgroup.com

Target Market(s)

Stock Brokerage Firms and Investment Advisers

Industry/Entity Type

Financial Service

Contact Information for Business Card

Russell K. Halvering
President
42 W. Calloway Blvd., Suite 300
Pasadena, CA 91847
O 626.555.0147 ext. 204
C 818.555.0192
Email: russ@halveringpartnersgroup.com
www.halveringpartnersgroup.com

Requirements
Nice to have
• The back of the card could be black with the logo with the white letters.
• I do want the front of the card to at least have the color logo with the black "Halvering & Partners Lettering.

```html
<!DOCTYPE html>
<html lang="en">
<head>
<meta charset="utf-8">
<title>Halvering &amp; Partners – Business Card</title>
<link href="https://fonts.googleapis.com/css2?family=Open+Sans:wght@400;600&display=swap" rel="stylesheet">
<style>
  :root {
    --ink: #0b0b0b;
    --paper: #ffffff;
    --accent: #b3121f;
    --backdrop: #e4e4e4;
    --font: "Open Sans", Arial, sans-serif;
  }
  * { margin: 0; padding: 0; box-sizing: border-box; }
  html, body { width: 1200px; height: 900px; overflow: hidden; }
  body { background: var(--backdrop); font-family: var(--font); position: relative; }

  .card {
    position: absolute;
    width: 600px;
    height: 343px;
    overflow: hidden;
    box-shadow: 0 6px 18px rgba(0,0,0,.25);
  }

  /* Back */
  .card-back { left: 540px; top: 70px; background: var(--ink); }
  .card-back .brand { position: absolute; left: 0; right: 0; top: 120px; justify-content: center; }
  .card-back .brand-name { color: var(--paper); }
  .card-back .url {
    position: absolute; left: 0; right: 0; top: 232px;
    text-align: center; color: var(--paper); font-size: 15px; letter-spacing: .5px;
  }

  /* Brand lockup */
  .brand { display: flex; align-items: center; gap: 16px; }
  .brand-mark { width: 46px; height: 46px; background: var(--accent); flex: none; }
  .brand-name { font-size: 32px; font-weight: 600; letter-spacing: 1px; }

  /* Front */
  .card-front { left: 60px; top: 480px; background: var(--paper); }
  .card-front .bands { position: absolute; inset: 0; }
  .card-front .brand { position: absolute; left: 34px; top: 36px; }
  .card-front .brand-name { color: var(--ink); }

  .address {
    position: absolute; left: 22px; top: 210px;
    color: var(--paper); font-size: 14px; line-height: 1.4; font-style: normal;
  }
  .person { position: absolute; right: 44px; top: 224px; text-align: right; }
  .person-name { color: var(--paper); font-size: 22px; line-height: 1.15; }
  .person-title { color: var(--accent); font-size: 15px; font-weight: 600; line-height: 1.2; }

  .contacts {
    position: absolute; right: 22px; top: 274px;
    list-style: none; color: var(--paper); font-size: 12.5px; line-height: 15px;
  }
  .contacts li { display: flex; justify-content: flex-end; align-items: center; gap: 10px; }
  .contacts svg { width: 12px; height: 12px; fill: var(--accent); flex: none; }
</style>
</head>
<body>

<section class="card card-back" aria-label="Card back">
  <div class="brand">
    <span class="brand-mark"></span>
    <span class="brand-name">Halvering &amp; Partners</span>
  </div>
  <p class="url">www.halveringpartnersgroup.com</p>
</section>

<section class="card card-front" aria-label="Card front">
  <svg class="bands" viewBox="0 0 600 343" width="600" height="343" aria-hidden="true">
    <path d="M0,120 Q320,290 600,110 L600,343 L0,343 Z" fill="var(--ink)"/>
    <path d="M290,205 Q480,212 600,104 L600,115 Q480,218 290,208 Z" fill="var(--accent)"/>
  </svg>

  <div class="brand">
    <span class="brand-mark"></span>
    <span class="brand-name">Halvering &amp; Partners</span>
  </div>

  <address class="address">
    42 W. Calloway Blvd., Suite 300<br>
    Pasadena, CA 91847
  </address>

  <div class="person">
    <p class="person-name">Russell K. Halvering</p>
    <p class="person-title">President</p>
  </div>

  <ul class="contacts">
    <li>626.555.0147 ext. 204
      <svg viewBox="0 0 24 24"><path d="M6.6 10.8a15 15 0 0 0 6.6 6.6l2.2-2.2a1 1 0 0 1 1-.25 11.4 11.4 0 0 0 3.6.57 1 1 0 0 1 1 1V20a1 1 0 0 1-1 1A17 17 0 0 1 3 4a1 1 0 0 1 1-1h3.5a1 1 0 0 1 1 1c0 1.25.2 2.45.57 3.57a1 1 0 0 1-.25 1z"/></svg>
    </li>
    <li>818.555.0192
      <svg viewBox="0 0 24 24"><path d="M7 1h10a2 2 0 0 1 2 2v18a2 2 0 0 1-2 2H7a2 2 0 0 1-2-2V3a2 2 0 0 1 2-2zm0 3v14h10V4zm5 15.5a1 1 0 1 0 0 2 1 1 0 0 0 0-2z"/></svg>
    </li>
    <li>russ@halveringpartnersgroup.com
      <svg viewBox="0 0 24 24"><path d="M2 5h20v14H2zm2 2v.5l8 5 8-5V7l-8 5z"/></svg>
    </li>
    <li>www.halveringpartnersgroup.com
      <svg viewBox="0 0 24 24"><path d="M12 2a10 10 0 1 0 0 20 10 10 0 0 0 0-20zm6.9 6h-3a15 15 0 0 0-1.3-3.9A8 8 0 0 1 18.9 8zM12 4c.8 1.2 1.5 2.5 1.9 4h-3.8c.4-1.5 1.1-2.8 1.9-4zM4.3 14a8 8 0 0 1 0-4h3.4a16 16 0 0 0 0 4zm.8 2h3a15 15 0 0 0 1.3 3.9A8 8 0 0 1 5.1 16zm3-8h-3a8 8 0 0 1 4.3-3.9A15 15 0 0 0 8.1 8zM12 20c-.8-1.2-1.5-2.5-1.9-4h3.8c-.4 1.5-1.1 2.8-1.9 4zm2.3-6H9.7a14 14 0 0 1 0-4h4.6a14 14 0 0 1 0 4zm.3 5.9a15 15 0 0 0 1.3-3.9h3a8 8 0 0 1-4.3 3.9zm1.7-5.9a16 16 0 0 0 0-4h3.4a8 8 0 0 1 0 4z"/></svg>
    </li>
  </ul>
</section>

</body>
</html>
```